Real Estate Team Needs Business Cards

Double sided - Team Member on Front, Team Leader on Back (back side will contain more details).
Colors to use:
Red = R: 233 G: 1 B: 2
Grey = R: 89 G: 89 B: 89
Black= R: 0 B: 0 B: 0
** MAIN FOCUS ** ( separate border, color, design, etc. to really stand out - whatever you think draws the most attention ) on both sides for "Sell for 1%‡" and "Buy & receive up to a 1% rebate‡". Must have fine print **
**Please make both sides stand out and look unique / different
Business card to have round corners (standard size 3.5" x 2").:
Document Trim Size
89 x 51 mm
1050 x 600 pixels
Full Bleed Size
92 x 54 mm
1085 x 635 pixels
Basic example provided. Please redesign as you see best. In your design - Please use the same picture on both sides. Name, address, phone number, email, etc. will be provided to the selected design. QR code on back side only if there is room (not important)

```html
<!DOCTYPE html>
<html lang="en">
<head>
<meta charset="UTF-8">
<title>Summit Line Realty – Business Cards</title>
<link href="https://fonts.googleapis.com/css2?family=Roboto:wght@300;400;700&display=swap" rel="stylesheet">
<style>
  :root {
    --red: rgb(233, 1, 2);
    --grey: rgb(89, 89, 89);
    --black: #000;
    --white: #fff;
    --stage: #e9e7e4;
    --suit-dark: #1f3567;
    --photo-light: #ffffff;
  }
  * { box-sizing: border-box; margin: 0; padding: 0; }
  html, body {
    width: 1200px; height: 716px; overflow: hidden;
    background: var(--stage);
    font-family: "Roboto", sans-serif;
  }
  .stage {
    width: 1200px; height: 716px;
    display: flex; align-items: center; justify-content: center; gap: 48px;
  }
  .card {
    position: relative; width: 540px; height: 309px;
    border-radius: 14px; overflow: hidden;
    box-shadow: 0 6px 18px rgba(0,0,0,.18);
  }
  .brand {
    display: flex; align-items: center; gap: 8px;
    font-weight: 700; font-size: 22px; letter-spacing: .5px; text-transform: uppercase;
    white-space: nowrap;
  }
  .brand-mark { width: 14px; height: 14px; background: var(--red); flex: none; }
  .brand-rule { position: absolute; height: 2px; background: var(--red); }

  /* Back side */
  .card-back { background: var(--black); color: var(--white); }
  .card-back .brand { position: absolute; top: 36px; left: 0; right: 0; justify-content: center; color: var(--white); }
  .card-back .brand-rule { top: 74px; left: 150px; width: 240px; }
  .offers {
    position: absolute; top: 100px; left: 0; right: 0; text-align: center;
    color: var(--red); font-weight: 700; font-size: 19px; line-height: 1.35;
  }
  .perks {
    position: absolute; top: 170px; left: 0; right: 0; text-align: center;
    list-style: none; font-weight: 300; font-size: 17px; line-height: 1.3;
  }
  .perks li::before { content: "• "; color: var(--red); }
  .back-band { position: absolute; left: 0; right: 0; bottom: 0; height: 12px; background: var(--red); }

  /* Front side */
  .card-front { background: var(--white); color: var(--grey); }
  .card-front .brand { position: absolute; top: 30px; left: 32px; color: var(--black); font-size: 20px; }
  .card-front .brand-rule { top: 64px; left: 32px; width: 250px; }
  .person { position: absolute; top: 82px; left: 32px; }
  .person-name { color: var(--red); font-weight: 700; font-size: 20px; }
  .person-role { font-size: 15px; margin-top: 2px; }
  .contacts {
    position: absolute; top: 140px; left: 32px;
    list-style: none; font-size: 15px; line-height: 21px;
  }
  .contacts li { display: flex; align-items: center; gap: 9px; white-space: nowrap; }
  .contacts svg { width: 12px; height: 12px; fill: var(--red); flex: none; }
  .accent { color: var(--red); }
  .address { position: absolute; top: 236px; left: 32px; font-size: 15px; white-space: nowrap; }
  .front-band { position: absolute; left: 0; bottom: 0; width: 300px; height: 6px; background: var(--red); }
  .portrait {
    position: absolute; right: 0; top: 70px; width: 235px; height: 239px;
    background: linear-gradient(180deg, var(--photo-light) 0%, var(--photo-light) 35%, #9aa7c0 62%, var(--suit-dark) 100%);
  }
</style>
</head>
<body>
<main class="stage">
  <section class="card card-back">
    <div class="brand"><span class="brand-mark"></span>Summit Line Realty</div>
    <div class="brand-rule"></div>
    <p class="offers">·Sell for 1%‡<br>·Buy &amp; receive up to a 1% rebate‡</p>
    <ul class="perks">
      <li>Free Homeevaluation</li>
      <li>Free Local Sold Reports</li>
      <li>Advanced Property Search</li>
    </ul>
    <div class="back-band"></div>
  </section>

  <section class="card card-front">
    <div class="brand"><span class="brand-mark"></span>Summit Line Realty</div>
    <div class="brand-rule"></div>
    <div class="person">
      <p class="person-name">Daniel Marsh</p>
      <p class="person-role">Manager</p>
    </div>
    <ul class="contacts">
      <li><svg viewBox="0 0 12 12"><path d="M3 0h6v12H3zM4 1.5v8h4v-8z"/></svg><span>123-456-2100</span></li>
      <li><svg viewBox="0 0 12 12"><path d="M2 0l3 3-1.5 1.5a7 7 0 0 0 4 4L9 7l3 3-2 2C5 12 0 7 0 2z"/></svg><span>123-456-2100</span></li>
      <li><svg viewBox="0 0 12 12"><path d="M0 2h12v8H0zM1 3l5 4 5-4z"/></svg><span>youremail@mailbox.com</span></li>
      <li><svg viewBox="0 0 12 12"><circle cx="6" cy="6" r="6"/></svg><span>www.<span class="accent">yourwebsite</span>.com</span></li>
    </ul>
    <p class="address">Your address, city, state, ZIP 0000</p>
    <div class="front-band"></div>
    <div class="portrait" role="img" aria-label="Portrait photo of the team manager in a blue suit"></div>
  </section>
</main>
</body>
</html>
```